Building Company Business Card Design

Need a design for a business card:
It needs to have: Name, Phone, Facebook link, Website, email
i would also like a list of works we undertake:
-New Homes
-Extensions, Renovations & Bathrooms
-Decking, Carports, Sheds (Residential and Industrial)
-Carpentry
-Fences, Patios & Pergolas

Contact Information for Business Card

Name, Phone, Facebook link, Website, email + details of services provided listed in description

```html
<!DOCTYPE html>
<html lang="en">
<head>
<meta charset="utf-8">
<title>Ridgeline Homes – Business Card</title>
<link href="https://fonts.googleapis.com/css2?family=Arimo:wght@400;700&display=swap" rel="stylesheet">
<style>
  :root {
    --page: #e9e6e1;
    --card: #070808;
    --band: #0c1f12;
    --band-deep: #0a1a0f;
    --shade: #131515;
    --green: #3ab54a;
    --rule: #1f6b2b;
    --white: #f2f2f2;
    --grey: #8d8f91;
  }
  * { box-sizing: border-box; margin: 0; padding: 0; }
  html, body { width: 1200px; height: 900px; overflow: hidden; }
  body {
    background: var(--page);
    font-family: "Arimo", Arial, sans-serif;
    display: flex; flex-direction: column; align-items: center; justify-content: center; gap: 36px;
  }
  .card {
    position: relative; width: 700px; height: 400px; border-radius: 30px;
    background: var(--card); overflow: hidden; color: var(--white);
    box-shadow: 0 10px 24px rgba(0,0,0,.25);
  }
  .card__backdrop { position: absolute; inset: 0; width: 100%; height: 100%; }
  .brand {
    position: absolute; display: flex; align-items: center; gap: 14px;
    color: var(--white); font-weight: 700; letter-spacing: .5px; line-height: 1.05;
  }
  .brand__mark { width: 18px; height: 18px; background: var(--green); flex: none; }
  .brand__name { font-size: 34px; }
  .brand__name small { display: block; font-size: 17px; letter-spacing: 1px; }
  .rule { position: absolute; height: 1px; background: var(--rule); }

  /* front */
  .front .brand { top: 52px; right: 48px; }
  .front .rule { top: 150px; left: 250px; right: 48px; }
  .services { position: absolute; top: 170px; right: 48px; text-align: right; }
  .services__title { color: var(--grey); font-weight: 700; font-size: 15px; letter-spacing: 1px; margin-bottom: 8px; }
  .services__list { list-style: none; font-size: 18px; line-height: 1.5; }

  /* back */
  .person { position: absolute; top: 130px; left: 44px; }
  .person__name { color: var(--green); font-weight: 700; font-size: 24px; letter-spacing: .5px; }
  .person__role { font-size: 19px; margin-top: 4px; }
  .contacts { position: absolute; top: 60px; right: 48px; list-style: none; font-size: 19px; line-height: 1; }
  .contacts li { display: flex; align-items: center; gap: 12px; margin-bottom: 11px; }
  .contacts svg { width: 18px; height: 18px; flex: none; fill: var(--green); }
  .back .rule { top: 255px; left: 300px; right: 48px; }
  .back .brand { top: 276px; right: 48px; }
</style>
</head>
<body>

<section class="card front">
  <svg class="card__backdrop" viewBox="0 0 700 400" aria-hidden="true">
    <polygon points="0,160 120,160 560,400 0,400" fill="var(--band)"/>
    <polygon points="0,170 40,170 40,400 0,400" fill="var(--shade)"/>
    <polygon points="0,320 220,400 0,400" fill="var(--band-deep)"/>
  </svg>
  <div class="brand">
    <span class="brand__mark"></span>
    <span class="brand__name">RIDGELINE HOMES<small>AND DEVELOPMENTS PTY LTD</small></span>
  </div>
  <div class="rule"></div>
  <div class="services">
    <p class="services__title">OUR SERVICES</p>
    <ul class="services__list">
      <li>New Homes, Extensions</li>
      <li>Renovations &amp; Bathrooms, Decking</li>
      <li>Carports, Sheds (Residential and Industrial)</li>
      <li>Carpentry, Fences, Patios &amp; Pergolas</li>
    </ul>
  </div>
</section>

<section class="card back">
  <svg class="card__backdrop" viewBox="0 0 700 400" aria-hidden="true">
    <polygon points="0,200 140,200 500,400 0,400" fill="var(--band)"/>
    <polygon points="0,210 40,210 40,400 0,400" fill="var(--shade)"/>
    <polygon points="0,330 200,400 0,400" fill="var(--band-deep)"/>
  </svg>
  <div class="person">
    <p class="person__name">JOHN SMITH</p>
    <p class="person__role">Director</p>
  </div>
  <ul class="contacts">
    <li><svg viewBox="0 0 24 24"><path d="M6.6 10.8a15 15 0 0 0 6.6 6.6l2.2-2.2a1 1 0 0 1 1-.25 11.4 11.4 0 0 0 3.6.6 1 1 0 0 1 1 1V20a1 1 0 0 1-1 1A17 17 0 0 1 3 4a1 1 0 0 1 1-1h3.5a1 1 0 0 1 1 1c0 1.25.2 2.45.6 3.6a1 1 0 0 1-.25 1z"/></svg>000-000-0000</li>
    <li><svg viewBox="0 0 24 24"><path d="M2 5h20v14H2z M3.5 6.5 12 13l8.5-6.5" fill="none" stroke="var(--green)" stroke-width="2"/></svg>info@ridgelinehomes.com</li>
    <li><svg viewBox="0 0 24 24"><g fill="none" stroke="var(--green)" stroke-width="1.8"><circle cx="12" cy="12" r="9"/><ellipse cx="12" cy="12" rx="4" ry="9"/><path d="M3 12h18M5 7h14M5 17h14"/></g></svg>www.ridgelinehomes.com</li>
    <li><svg viewBox="0 0 24 24"><path d="M12 2a7 7 0 0 0-7 7c0 5 7 13 7 13s7-8 7-13a7 7 0 0 0-7-7zm0 9.5A2.5 2.5 0 1 1 12 6.5a2.5 2.5 0 0 1 0 5z"/></svg>00 dummy city, dummy place 0000</li>
    <li><svg viewBox="0 0 24 24"><circle cx="12" cy="12" r="10"/></svg>Ridgelinehomes/</li>
  </ul>
  <div class="rule"></div>
  <div class="brand">
    <span class="brand__mark"></span>
    <span class="brand__name">RIDGELINE HOMES<small>AND DEVELOPMENTS PTY LTD</small></span>
  </div>
</section>

</body>
</html>
```